Pel'k Marrowind Travel

We need a sleek, professional, inviting card to elicit global travel for the experienced and professional traveler. Royal blue, black and silver. (perhaps the wording could be silver with black shadow?-get creative) Maybe a watermark on the front and the full raised logo on the back.
We want a stylish and modern card, but professional.

```html
<!DOCTYPE html>
<html lang="en">
<head>
<meta charset="UTF-8">
<title>Pel'k Marrowind Travel — Business Card</title>
<link href="https://fonts.googleapis.com/css2?family=Roboto:wght@400;500;700&display=swap" rel="stylesheet">
<style>
  :root {
    --stage: #e9ebee;
    --sky-blue: #27a8e0;
    --leaf-green: #8cc63f;
    --ink: #3a3a3a;
    --paper: #ffffff;
    --watermark: rgba(39, 168, 224, 0.10);
  }
  * { box-sizing: border-box; margin: 0; padding: 0; }
  html, body {
    width: 1200px; height: 960px; overflow: hidden;
    background: var(--stage);
    font-family: "Roboto", Arial, sans-serif;
  }
  .canvas {
    position: relative; width: 1200px; height: 960px;
  }
  .card {
    position: absolute; left: 300px;
    width: 600px; height: 343px;
    border-radius: 22px;
    box-shadow: 0 6px 18px rgba(0,0,0,0.12);
    overflow: hidden;
  }
  .card--back { top: 80px; background: var(--sky-blue); }
  .card--front { top: 510px; background: var(--paper); }

  .brand-name {
    position: absolute;
    font-weight: 700;
    letter-spacing: 0.5px;
    text-transform: uppercase;
    text-align: right;
    line-height: 1.15;
  }
  .card--back .brand-name {
    right: 36px; bottom: 40px;
    color: var(--paper);
    font-size: 24px;
  }
  .card--front .brand-name {
    right: 36px; top: 40px;
    color: var(--sky-blue);
    font-size: 24px;
  }
  .brand-rule {
    position: absolute; height: 2px; width: 230px; right: 36px;
  }
  .card--back .brand-rule { bottom: 30px; background: var(--paper); }
  .card--front .brand-rule { top: 104px; background: var(--leaf-green); }

  .watermark {
    position: absolute; right: 30px; top: 140px;
    font-weight: 700; font-size: 54px; line-height: 1;
    color: var(--watermark); text-transform: uppercase; text-align: right;
  }

  .holder { position: absolute; left: 40px; top: 130px; }
  .holder__name { color: var(--sky-blue); font-weight: 700; font-size: 22px; }
  .holder__role { color: var(--leaf-green); font-size: 16px; margin-top: 4px; }

  .contact { position: absolute; left: 40px; top: 200px; color: var(--ink); font-size: 16px; line-height: 1.3; }
  .contact__label { color: var(--sky-blue); font-weight: 500; }
  .contact__list { list-style: none; margin-top: 10px; }
  .contact__item { display: flex; align-items: center; gap: 10px; }
  .contact__icon { width: 13px; height: 13px; fill: var(--sky-blue); flex: none; }
</style>
</head>
<body>
<main class="canvas">
  <section class="card card--back" aria-label="Card back">
    <p class="brand-name">Pel'k Marrowind<br>Travel</p>
    <div class="brand-rule"></div>
  </section>

  <section class="card card--front" aria-label="Card front">
    <p class="brand-name">Pel'k Marrowind<br>Travel</p>
    <div class="brand-rule"></div>
    <p class="watermark" aria-hidden="true">Pel'k</p>

    <div class="holder">
      <p class="holder__name">Dorian Vesselmark</p>
      <p class="holder__role">Founder &amp; CEO</p>
    </div>

    <div class="contact">
      <p class="contact__label">Address:</p>
      <p>48 Harbor Crest Lane</p>
      <p>Suite #C, Halvern, OR 97310</p>
      <ul class="contact__list">
        <li class="contact__item">
          <svg class="contact__icon" viewBox="0 0 24 24" aria-hidden="true"><path d="M6.6 10.8a15.1 15.1 0 0 0 6.6 6.6l2.2-2.2a1 1 0 0 1 1-.25 11.4 11.4 0 0 0 3.6.57 1 1 0 0 1 1 1V20a1 1 0 0 1-1 1A17 17 0 0 1 3 4a1 1 0 0 1 1-1h3.5a1 1 0 0 1 1 1c0 1.25.2 2.45.57 3.57a1 1 0 0 1-.25 1z"/></svg>
          <span>503-218-4470</span>
        </li>
        <li class="contact__item">
          <svg class="contact__icon" viewBox="0 0 24 24" aria-hidden="true"><path d="M2 5h20v14H2z M2 5l10 8 10-8" /></svg>
          <span>hello@pelkmarrowind.com</span>
        </li>
        <li class="contact__item">
          <svg class="contact__icon" viewBox="0 0 24 24" aria-hidden="true"><circle cx="12" cy="12" r="10"/></svg>
          <span>www.pelkmarrowind.com</span>
        </li>
      </ul>
    </div>
  </section>
</main>
</body>
</html>
```